German Headhunter/ HR Consultancy needs Business Cards Design

We need a business Card Design for our Company in Stuttgart. We are specialized as Headhunter/ HR Consultancy in Placement of specialist and managers in permanent employment. Please refer to our business logo.

```html
<!DOCTYPE html>
<html lang="de">
<head>
<meta charset="utf-8">
<title>Nordfeld Personalberatung – Visitenkarte</title>
<link rel="stylesheet" href="https://fonts.googleapis.com/css2?family=Montserrat:wght@600;700&family=Arimo:wght@400&display=swap">
<style>
  :root {
    --brand-blue: #3953a6;
    --brand-grey: #8e9095;
    --ink: #1f1f24;
    --paper: #ffffff;
    --backdrop: #232323;
  }
  * { box-sizing: border-box; margin: 0; padding: 0; }
  html, body { width: 1200px; height: 988px; overflow: hidden; }
  body {
    background: var(--backdrop);
    position: relative;
    font-family: "Arimo", Arial, sans-serif;
  }
  .card {
    position: absolute;
    width: 560px;
    height: 320px;
    border-radius: 18px;
    overflow: hidden;
  }
  .card--back { left: 60px; top: 90px; background: var(--brand-blue); }
  .card--front { left: 580px; top: 570px; background: var(--paper); }

  .wordmark {
    position: absolute;
    display: flex;
    align-items: center;
    gap: 14px;
    font-family: "Montserrat", sans-serif;
    font-weight: 700;
    letter-spacing: 1px;
    text-transform: uppercase;
    line-height: 1;
  }
  .wordmark__square { width: 40px; height: 40px; flex: none; }
  .wordmark__name { font-size: 30px; }
  .wordmark__sub { display: block; font-size: 15px; letter-spacing: 1.5px; margin-top: 6px; }

  .card--back .wordmark { left: 110px; top: 126px; color: var(--paper); }
  .card--back .wordmark__square { background: var(--paper); }

  .card--front .wordmark { left: 140px; top: 56px; color: var(--brand-blue); }
  .card--front .wordmark__square { background: var(--brand-blue); }

  .holder {
    position: absolute;
    left: 52px;
    top: 160px;
    width: 210px;
    text-align: right;
  }
  .holder__name {
    font-family: "Montserrat", sans-serif;
    font-weight: 700;
    font-size: 22px;
    color: var(--brand-blue);
    letter-spacing: 0.5px;
  }
  .holder__role { font-size: 13px; color: var(--ink); margin-top: 3px; }

  .divider {
    position: absolute;
    left: 280px;
    top: 146px;
    width: 1px;
    height: 76px;
    background: var(--brand-grey);
  }

  .contacts {
    position: absolute;
    left: 300px;
    top: 146px;
    list-style: none;
    font-size: 13px;
    color: var(--ink);
  }
  .contacts li { display: flex; align-items: center; gap: 8px; height: 26px; }
  .contacts svg { width: 13px; height: 13px; fill: var(--brand-blue); flex: none; }

  .address-band {
    position: absolute;
    left: 0; right: 0;
    top: 248px;
    height: 42px;
    background: var(--brand-blue);
    color: var(--paper);
    font-size: 14px;
    display: flex;
    align-items: center;
    justify-content: center;
    letter-spacing: 0.3px;
  }
</style>
</head>
<body>

  <section class="card card--back" aria-label="Rückseite">
    <div class="wordmark">
      <span class="wordmark__square"></span>
      <span>
        <span class="wordmark__name">Nordfeld</span>
        <span class="wordmark__sub">Personalberatung</span>
      </span>
    </div>
  </section>

  <section class="card card--front" aria-label="Vorderseite">
    <div class="wordmark">
      <span class="wordmark__square"></span>
      <span>
        <span class="wordmark__name">Nordfeld</span>
        <span class="wordmark__sub">Personalberatung</span>
      </span>
    </div>

    <div class="holder">
      <p class="holder__name">JONAS ALBRECHT</p>
      <p class="holder__role">CEO/Founder</p>
    </div>

    <span class="divider"></span>

    <ul class="contacts">
      <li>
        <svg viewBox="0 0 24 24" aria-hidden="true"><path d="M6.6 10.8a15.1 15.1 0 0 0 6.6 6.6l2.2-2.2a1 1 0 0 1 1-.25 11.4 11.4 0 0 0 3.6.57 1 1 0 0 1 1 1V20a1 1 0 0 1-1 1A17 17 0 0 1 3 4a1 1 0 0 1 1-1h3.5a1 1 0 0 1 1 1c0 1.25.2 2.45.57 3.57a1 1 0 0 1-.25 1z"/></svg>
        (555) 010 - 2846
      </li>
      <li>
        <svg viewBox="0 0 24 24" aria-hidden="true"><path d="M2 5h20v14H2zM12 12.5 3.5 6.5v1.8L12 14.3l8.5-6V6.5z"/></svg>
        info@nordfeld-beratung.de
      </li>
      <li>
        <svg viewBox="0 0 24 24" aria-hidden="true"><circle cx="12" cy="12" r="10"/></svg>
        www.nordfeld-beratung.de
      </li>
    </ul>

    <div class="address-band">220 Lindenweg Suite B Musterland, 7012</div>
  </section>

</body>
</html>
```